Modern Employee Handbook Cover Design Needed

I need help. I am designing a 50+ page Employee Handbook and want a great cover design. I'm looking for a great cover because our company has changed so much in the past years since the last handbook was published and I want to signify and celebrate all the positive things we have done. It may not seem like such a big deal but I'm trying to make a big impact.

I'm looking for something interesting. Employee Handbooks are the most boring things int he world but I don't ours to LOOK that way. I want creative, modern, slick, clean, whatever you want that would make someone want to look at (even if it is for a second). It does NOT need to even be called an Employee Handbook (I'm really open to ideas)

This will be a typical 8.5 x 11 book format. 70% of our employees are under the age of 40 and are in CA, MA, FL, and IN.

The final design should communicate that we are not the same company we were a few years ago but instead we are more modern and current.

Target Market(s)

Most of our employees are under 40 years old. They are well educated. We are a national company with employees in CA, MA, FL and IN

Industry/Entity Type

Education

Font styles to use
Serif
Sans Serif
Other font styles liked:
• I like the fonts used by velmo but am open to ANY fonts.

Requirements
Must have
• Modern, up to date designs, unexpected, unique, cool, etc...
Should not have
• I don't like the typical teamwork images, world and globe things, or tree supporting branch type things that Human Resources and Employee Handbooks often is represented by in print. They are so boring to me. https://www.trelvasearch.com/search?q=human+resources+handbook&source=lnms&tbm=isch&sa=X&ved=0ahUKEwjl1oWHt67RAhULw1QKHWTaB0oQ_AUICCgB&biw=1920&bih=950
• No stick figures standing in a row or shaking hands. Stuff like that is so old.
• Our clients are young adults with Autism but I don't want puzzle pieces which is a universal symbol of Autism.

```html
<!DOCTYPE html>
<html lang="en">
<head>
<meta charset="utf-8">
<title>KVR Employee Handbook</title>
<link href="https://fonts.googleapis.com/css2?family=Alfa+Slab+One&family=Fira+Sans:wght@700&family=Fira+Sans+Condensed:wght@300&display=swap" rel="stylesheet">
<style>
  :root {
    --cover-cyan: #4de3ff;
    --paper-white: #ffffff;
    --subtitle-aqua: #93f2ff;
  }
  html, body {
    margin: 0;
    padding: 0;
    width: 927px;
    height: 1200px;
    overflow: hidden;
    background: var(--cover-cyan);
  }
  .cover {
    position: relative;
    width: 927px;
    height: 1200px;
    background: var(--cover-cyan);
  }
  .cover-art {
    position: absolute;
    inset: 0;
    display: block;
  }
  .company-name {
    font-family: "Alfa Slab One", "Rockwell", serif;
    fill: var(--paper-white);
  }
  .handbook-title {
    font-family: "Fira Sans", "Helvetica Neue", sans-serif;
    font-weight: 700;
    fill: var(--subtitle-aqua);
  }
  .quote-bubble {
    fill: none;
    stroke: var(--paper-white);
    stroke-width: 3;
    stroke-linejoin: round;
  }
  .quote-text {
    font-family: "Fira Sans Condensed", "Arial Narrow", sans-serif;
    font-weight: 300;
    font-size: 21px;
    fill: var(--paper-white);
  }
  .quote-author {
    font-family: "Fira Sans Condensed", "Arial Narrow", sans-serif;
    font-weight: 300;
    font-size: 16px;
    fill: var(--paper-white);
  }
</style>
</head>
<body>
<main class="cover">
  <svg class="cover-art" width="927" height="1200" viewBox="0 0 927 1200" xmlns="http://www.w3.org/2000/svg">
    <text class="company-name" x="62" y="410" font-size="455" textLength="778" lengthAdjust="spacingAndGlyphs">KVR</text>
    <text class="handbook-title" x="370" y="454" font-size="35" textLength="348" lengthAdjust="spacingAndGlyphs">EMPLOYEE HANDBOOK</text>

    <path class="quote-bubble" d="M700 893
      C780 886 855 915 860 975
      C864 1022 838 1048 814 1059
      L824 1103
      L789 1070
      C740 1078 680 1083 630 1080
      C570 1076 515 1050 511 1000
      C507 940 560 905 620 898
      C650 894 675 894 700 893 Z"/>
    <text class="quote-text" x="559" y="964">If you think you are too small</text>
    <text class="quote-text" x="559" y="996">to make a difference,</text>
    <text class="quote-text" x="559" y="1037">try sleeping with a mosquito.</text>
    <text class="quote-author" x="882" y="1148" text-anchor="end">Sonam Reyal</text>
  </svg>
</main>
</body>
</html>
```